The Silver Lantern book cover

To design an e-book and printed cover that will initially be used on Brellow for Quillet.

My website www.thesilverlantern-example.com

Full title
The Silver Lantern - Start your own success journey in '4 simple steps'.
Subtitle: Everything from understanding your subconscious mind to setting out an action plan for your future.

The Silver Lantern part although it's the beginning of the title will be the smaller part, the rest will be the focus.

I want a clean modern feel, take inspiration from the top self-help books currently on Brellow. Clean crisp and bold.

The book is about setting goals and navigating a complicated road of obstacles in order to achieve them. If this can be illustrated in the graphic or on the cover that would be a bonus.

Requirements for the size of your cover art must have an ideal height/width ratio of at least 1.6, meaning:

• A minimum of 625 pixels on the shortest side and 1000 pixels on the longest side
• For best quality, your image should be 2500 pixels on the longest side
Updates

Reason: Going to go through last time give feedback and any changes before I pick 3 to get a poll done. Loving the ideas and designs. New designs welcome, please put all emphasis on the subheading 'start your...' Have a great Christmas if you celebrate.

Target Market(s)

Target market would be middle age male and females.

Industry/Entity Type

Moving

Font styles to use
Serif
Sans Serif

Requirements
Must have
• Must have the full title even if it is split.

Author name Dorian Falk
Nice to have
• The photo of author but not sure whether to use it or not.

Graphics like moving roads and suchlike.

```html
<!DOCTYPE html>
<html lang="en">
<head>
<meta charset="utf-8">
<title>The Silver Lantern — Book Cover</title>
<link rel="stylesheet" href="https://fonts.googleapis.com/css2?family=Montserrat:wght@600;700&family=Arimo:wght@400;700&display=swap">
<style>
  :root {
    --page: #ffffff;
    --back: #000000;
    --ink-light: #ffffff;
    --sky-top: #3d5b8c;
    --sky-mid: #8a9fb8;
    --horizon: #f4d7a4;
    --glow: #fff3d6;
    --hill: #4a5a24;
    --road: #2c2a2a;
    --portrait-a: #d9d9d9;
    --portrait-b: #9a9a9a;
  }
  * { margin: 0; padding: 0; box-sizing: border-box; }
  html, body { width: 1200px; height: 1000px; overflow: hidden; background: var(--page); }
  .canvas { position: relative; width: 1200px; height: 1000px; background: var(--page); }

  .back-cover {
    position: absolute; left: 58px; top: 127px; width: 508px; height: 766px;
    background: var(--back);
  }
  .author-portrait {
    position: absolute; left: 38px; top: 27px; width: 181px; height: 207px;
    background: linear-gradient(160deg, var(--portrait-a) 0%, #c4c4c4 50%, var(--portrait-b) 100%);
  }
  .back-copy {
    position: absolute; left: 35px; top: 250px; width: 442px;
    font-family: "Arimo", Arial, sans-serif; font-weight: 700; font-size: 11px;
    line-height: 15.4px; color: var(--ink-light); text-align: justify; hyphens: auto;
  }
  .back-copy p + p { margin-top: 15px; }

  .front-cover {
    position: absolute; left: 566px; top: 127px; width: 576px; height: 766px; overflow: hidden;
  }
  .cover-scene {
    position: absolute; inset: 0;
    background:
      radial-gradient(ellipse 300px 110px at 530px 480px, var(--glow) 0%, rgba(255,230,180,0.6) 40%, rgba(255,220,170,0) 100%),
      linear-gradient(180deg, var(--sky-top) 0%, #5a76a0 25%, var(--sky-mid) 45%, #c9b9a4 58%, var(--horizon) 64%, var(--hill) 68%, #3b3a26 78%, var(--road) 100%);
  }

  .spine-title {
    position: absolute; left: 16px; top: 38px; height: 318px; writing-mode: vertical-rl;
    font-family: "Montserrat", Arial, sans-serif; font-weight: 600; font-size: 27px;
    letter-spacing: 0.5px; color: var(--ink-light); white-space: nowrap;
  }
  .spine-subtitle {
    position: absolute; left: 29px; top: 370px; writing-mode: vertical-rl;
    font-family: "Arimo", Arial, sans-serif; font-size: 11px; line-height: 13px;
    color: var(--ink-light); white-space: nowrap;
  }
  .spine-author {
    position: absolute; left: 18px; top: 598px; writing-mode: vertical-rl;
    font-family: "Arimo", Arial, sans-serif; font-weight: 700; font-size: 17px;
    color: var(--ink-light); white-space: nowrap;
  }

  .cover-title {
    position: absolute; left: 56px; top: 30px; width: 520px; text-align: center;
    font-family: "Montserrat", Arial, sans-serif; font-weight: 600; font-size: 60px;
    line-height: 64px; color: var(--ink-light); text-shadow: 2px 2px 3px rgba(0,0,0,0.45);
  }
  .cover-tagline {
    position: absolute; left: 66px; top: 160px; width: 500px; text-align: center;
    font-family: "Arimo", Arial, sans-serif; font-size: 22px; line-height: 30px;
    color: var(--ink-light); text-shadow: 1px 1px 2px rgba(0,0,0,0.4); white-space: nowrap;
  }
  .cover-summary {
    position: absolute; left: 72px; top: 631px; width: 500px; text-align: center;
    font-family: "Arimo", Arial, sans-serif; font-weight: 700; font-size: 19px; line-height: 22px;
    color: var(--ink-light); text-shadow: 1px 1px 2px rgba(0,0,0,0.5); white-space: nowrap;
  }
  .cover-author {
    position: absolute; left: 72px; top: 719px; width: 500px; text-align: center;
    font-family: "Arimo", Arial, sans-serif; font-weight: 700; font-size: 16px;
    color: var(--ink-light);
  }
</style>
</head>
<body>
<div class="canvas">
  <section class="back-cover">
    <div class="author-portrait" role="img" aria-label="Portrait photograph of the author"></div>
    <div class="back-copy">
      <p>"Lorem ipsum dolor sit amet, consectetur adipiscing elit, sed do eiusmod tempor incididunt ut labore et dolore magna aliqua. Ut enim ad minim veniam, quis nostrud exercitation ullamco laboris nisi ut aliquip ex ea commodo consequat. Duis aute irure dolor in reprehenderit in voluptate velit esse cillum dolore eu fugiat nulla pariatur. Excepteur sint occaecat cupidatat non proident, sunt in culpa qui officia deserunt mollit anim id est laborum."</p>
      <p>"Sed ut perspiciatis unde omnis iste natus error sit voluptatem accusantium doloremque laudantium, totam rem aperiam, eaque ipsa quae ab illo inventore veritatis et quasi architecto beatae vitae dicta sunt explicabo. Nemo enim ipsam voluptatem quia voluptas sit aspernatur aut odit aut fugit, sed quia consequuntur magni dolores eos qui ratione voluptatem sequi nesciunt. Neque porro quisquam est, qui dolorem ipsum quia dolor sit amet, consectetur, adipisci velit, sed quia non numquam eius modi tempora incidunt ut labore et dolore magnam aliquam quaerat voluptatem. Ut enim ad minima veniam, quis nostrum exercitationem ullam corporis suscipit laboriosam, nisi ut aliquid ex ea commodi consequatur? Quis autem vel eum iure reprehenderit qui in ea voluptate velit esse quam nihil molestiae consequatur, vel illum qui dolorem eum fugiat quo voluptas nulla pariatur?"</p>
    </div>
  </section>

  <section class="front-cover">
    <div class="cover-scene" role="img" aria-label="Photograph of an open road running toward a misty sunrise between green hills"></div>
    <div class="spine-title">THE SILVER LANTERN</div>
    <div class="spine-subtitle">Start your own success journey<br>in '4 simple steps'</div>
    <div class="spine-author">DORIAN FALK</div>

    <h1 class="cover-title">THE SILVER<br>LANTERN</h1>
    <p class="cover-tagline">Start your own success journey<br>in '4 simple steps'</p>
    <p class="cover-summary">Everything from understanding<br>your subconscious mind to setting out<br>an action plan for your future.</p>
    <p class="cover-author">DORIAN FALK</p>
  </section>
</div>
</body>
</html>
```